Webbanner-Design für Affiliate Marketing
Zielgruppe
Online-Shop für Kopfbedeckungen aller Art (Hüte, Mützen, Fascinator, Stirnbänder)
Design soll eine möglichst große Zielgruppe ansprechen (Hauptfokus: 18-34 Jahre). Also alle Online-Shopper mit einer Vorliebe für Hüte/ Mützen.
Aufgabenstellung
Insgesamt ein modernes, eingängiges und stilvolles Design. Nicht allzu verspielt oder zu unruhig. Fokus auf das Wesentliche.
Text: A Headwear for Everyone
B Hüte und Mützen, Top Auswahl, Kostenlose Lieferung
C Gut behütet durch den Winter
D Der Hut-Online-Shop
Das Lorvo Fein Logo soll mit eingebunden werden. Keine vorgegebene Platzierung, sprich dem Design anpassen.
Formate: (Breite x Höhe)
1. Full Banner - 468 x 60 Pixel, max. 40k Dateigröße
2. Medium Rectangle - 300 x 250 Pixel, max. 40k Dateigröße
3. Vertical Banner - 120 x 240 Pixel, max. 30k Dateigröße
4. Rectangle - 180 x 150 Pixel, max. 40k Dateigröße

```html
<!DOCTYPE html>
<html lang="de">
<head>
<meta charset="utf-8">
<title>Lorvo Fein – Webbanner</title>
<link rel="stylesheet" href="https://fonts.googleapis.com/css2?family=Bodoni+Moda:wght@700&family=Poppins:wght@400&display=swap">
<style>
  :root {
    --page: #ffffff;
    --ink: #ffffff;
    --rule: rgba(255,255,255,0.85);
    --accent: #e5484b;
    --logo-bg: #ffffff;
    --logo-ink: #2a2a2a;
    --frame: #d9d9d9;
  }
  * { margin: 0; padding: 0; box-sizing: border-box; }
  html, body { width: 694px; height: 1200px; overflow: hidden; background: var(--page); }
  .stage {
    position: relative; width: 750px; height: 1297px;
    transform: scale(0.9253); transform-origin: 0 0;
  }
  .banner {
    position: absolute; overflow: hidden; border: 1px solid var(--frame);
    font-family: "Bodoni Moda", "Times New Roman", serif; color: var(--ink);
  }
  .photo { position: absolute; inset: 0; }
  .shade { position: absolute; inset: 0; background: linear-gradient(180deg, rgba(0,0,0,0.05) 0%, rgba(0,0,0,0.35) 100%); }
  .logo {
    position: absolute; left: 0; top: 0; background: var(--logo-bg);
    display: flex; align-items: center; justify-content: center; gap: 4px;
    font-family: "Bodoni Moda", "Times New Roman", serif; font-weight: 700;
    font-size: 10px; letter-spacing: 0.5px; color: var(--logo-ink);
  }
  .logo .dot { width: 9px; height: 9px; border-radius: 50%; background: var(--logo-ink); }
  .line { position: absolute; left: 9px; font-weight: 700; line-height: 1; white-space: nowrap; text-transform: uppercase; }
  .ruled { border-bottom: 1.5px solid var(--rule); padding-bottom: 3px; }
  .sub { position: absolute; left: 10px; font-size: 13px; font-weight: 700; line-height: 1; white-space: nowrap; }
  .cta {
    position: absolute; border: 2px solid var(--accent); color: var(--ink);
    font-family: "Poppins", Arial, sans-serif; font-weight: 400;
    display: flex; align-items: center; justify-content: center; white-space: nowrap;
  }
  .std .cta { left: 64px; top: 200px; width: 170px; height: 39px; font-size: 17px; }

  .tone-felt { background: linear-gradient(120deg, #3a3a38 0%, #5c5a4c 45%, #6e6a55 60%, #2a2a2a 100%); }
  .tone-plum { background: linear-gradient(120deg, #3d3b3a 0%, #6b5546 40%, #3b2a35 70%, #8a7a6a 100%); }
  .tone-mustard { background: linear-gradient(120deg, #6e6a66 0%, #8e7d6c 40%, #b9a23a 65%, #4a4440 100%); }
  .tone-wood { background: linear-gradient(120deg, #5a4a3c 0%, #3a3028 45%, #6a5040 70%, #2e2622 100%); }
  .tone-brick { background: linear-gradient(120deg, #9a7e78 0%, #8a6e66 45%, #3a2e2a 70%, #5e4a42 100%); }
  .tone-beanie { background: linear-gradient(120deg, #7e7a80 0%, #a29aa0 40%, #b8652e 62%, #4a4648 100%); }
  .tone-snow { background: linear-gradient(120deg, #8a7a70 0%, #5a5a4a 40%, #3e4a30 62%, #2e2e2a 100%); }
</style>
</head>
<body>
<div class="stage">

  <!-- Full Banner 468 x 60 -->
  <section class="banner" style="left:44px;top:50px;width:468px;height:60px;">
    <div class="logo" style="width:60px;height:60px;flex-direction:column;gap:3px;font-size:8px;border-right:1px solid var(--frame);"><span class="dot"></span><span>LORVO FEIN</span></div>
    <div class="photo tone-felt" style="left:60px;" role="img" aria-label="Hand hält einen olivgrünen Filzhut mit Lederband"></div>
    <div class="line ruled" style="left:160px;top:7px;font-size:17px;">Der Hut</div>
    <div class="line" style="left:160px;top:32px;font-size:20px;">Online Shop</div>
    <div class="cta" style="left:347px;top:15px;width:110px;height:30px;font-size:12px;">Jetzt kaufen</div>
  </section>

  <!-- Medium Rectangle 300 x 250 -->
  <section class="banner std" style="left:44px;top:140px;width:300px;height:250px;">
    <div class="photo tone-felt" role="img" aria-label="Hand hält einen olivgrünen Filzhut mit Lederband"></div>
    <div class="shade"></div>
    <div class="logo" style="width:85px;height:42px;"><span class="dot"></span><span>LORVO FEIN</span></div>
    <div class="line ruled" style="top:58px;font-size:30px;">Der Hut</div>
    <div class="line" style="top:100px;font-size:42px;">Online</div>
    <div class="line" style="top:140px;font-size:42px;">Shop</div>
    <div class="cta">Jetzt kaufen</div>
  </section>

  <!-- Vertical Banner 120 x 240 -->
  <section class="banner" style="left:374px;top:140px;width:120px;height:240px;">
    <div class="photo tone-felt" role="img" aria-label="Hand hält einen olivgrünen Filzhut mit Lederband"></div>
    <div class="shade"></div>
    <div class="logo" style="width:44px;height:50px;flex-direction:column;gap:3px;font-size:7px;"><span class="dot"></span><span>LORVO</span></div>
    <div class="line ruled" style="top:108px;font-size:18px;">Der Hut</div>
    <div class="line" style="top:134px;font-size:24px;">Online</div>
    <div class="line" style="top:158px;font-size:24px;">Shop</div>
    <div class="cta" style="left:9px;top:202px;width:100px;height:27px;font-size:11px;">Jetzt kaufen</div>
  </section>

  <!-- Rectangle 180 x 150 -->
  <section class="banner" style="left:524px;top:140px;width:180px;height:150px;">
    <div class="photo tone-felt" role="img" aria-label="Hand hält einen olivgrünen Filzhut mit Lederband"></div>
    <div class="shade"></div>
    <div class="logo" style="width:85px;height:33px;"><span class="dot"></span><span>LORVO FEIN</span></div>
    <div class="line ruled" style="top:50px;font-size:19px;">Der Hut</div>
    <div class="line" style="top:76px;font-size:21px;">Online Shop</div>
    <div class="cta" style="left:35px;top:110px;width:109px;height:29px;font-size:12px;">Jetzt kaufen</div>
  </section>

  <!-- A Headwear for Everyone -->
  <section class="banner std" style="left:44px;top:420px;width:300px;height:250px;">
    <div class="photo tone-plum" role="img" aria-label="Frau mit dunkelrotem Hut vor Holzwand"></div>
    <div class="shade"></div>
    <div class="logo" style="width:85px;height:42px;"><span class="dot"></span><span>LORVO FEIN</span></div>
    <div class="line" style="top:108px;font-size:35px;">A Headwear</div>
    <div class="line ruled" style="top:145px;font-size:35px;">For Everyone</div>
    <div class="cta">Jetzt kaufen</div>
  </section>
  <section class="banner std" style="left:374px;top:420px;width:300px;height:250px;">
    <div class="photo tone-mustard" role="img" aria-label="Frau mit breitkrempigem grauem Hut und gelber Jacke"></div>
    <div class="shade"></div>
    <div class="logo" style="width:85px;height:42px;"><span class="dot"></span><span>LORVO FEIN</span></div>
    <div class="line" style="top:108px;font-size:35px;">A Headwear</div>
    <div class="line ruled" style="top:145px;font-size:35px;">For Everyone</div>
    <div class="cta">Jetzt kaufen</div>
  </section>

  <!-- Hüte und Mützen -->
  <section class="banner std" style="left:44px;top:700px;width:300px;height:250px;">
    <div class="photo tone-wood" role="img" aria-label="Frau mit schwarzem Hut im Profil"></div>
    <div class="shade"></div>
    <div class="logo" style="width:85px;height:42px;"><span class="dot"></span><span>LORVO FEIN</span></div>
    <div class="line" style="top:68px;font-size:38px;">Hüte und</div>
    <div class="line ruled" style="top:110px;font-size:38px;">Mützen</div>
    <div class="sub" style="top:164px;">Top Auswahl · Kostenlose Lieferung</div>
    <div class="cta">Jetzt kaufen</div>
  </section>
  <section class="banner std" style="left:374px;top:700px;width:300px;height:250px;">
    <div class="photo tone-brick" role="img" aria-label="Mann mit braunem Hut vor Backsteinwand"></div>
    <div class="shade"></div>
    <div class="logo" style="width:85px;height:42px;"><span class="dot"></span><span>LORVO FEIN</span></div>
    <div class="line" style="top:68px;font-size:38px;">Hüte und</div>
    <div class="line ruled" style="top:110px;font-size:38px;">Mützen</div>
    <div class="sub" style="top:164px;">Top Auswahl · Kostenlose Lieferung</div>
    <div class="cta">Jetzt kaufen</div>
  </section>

  <!-- Gut behütet durch den Winter -->
  <section class="banner std" style="left:44px;top:980px;width:300px;height:250px;">
    <div class="photo tone-beanie" role="img" aria-label="Frau mit orangefarbener Strickmütze"></div>
    <div class="shade"></div>
    <div class="logo" style="width:85px;height:42px;"><span class="dot"></span><span>LORVO FEIN</span></div>
    <div class="line" style="top:56px;font-size:38px;">Gut</div>
    <div class="line" style="top:94px;font-size:38px;">Behütet</div>
    <div class="line" style="top:134px;font-size:22px;">Durch den</div>
    <div class="line ruled" style="top:157px;font-size:22px;">Winter</div>
    <div class="cta">Jetzt kaufen</div>
  </section>
  <section class="banner std" style="left:374px;top:980px;width:300px;height:250px;">
    <div class="photo tone-snow" role="img" aria-label="Person mit grünem Filzhut im Schneefall"></div>
    <div class="shade"></div>
    <div class="logo" style="width:85px;height:42px;"><span class="dot"></span><span>LORVO FEIN</span></div>
    <div class="line" style="top:56px;font-size:38px;">Gut</div>
    <div class="line" style="top:94px;font-size:38px;">Behütet</div>
    <div class="line" style="top:134px;font-size:22px;">Durch den</div>
    <div class="line ruled" style="top:157px;font-size:22px;">Winter</div>
    <div class="cta">Jetzt kaufen</div>
  </section>

</div>
</body>
</html>
```